Packaging for a new tea company

Hi guys we need a new packaging design for a tea company we are starting

Our competitors are leafora, zip an brew

I have uploaded pictures of our competitors for you to see the sample
The label need to be catchy

Our brand is called #JoinVividLeaf
We need two packaging designs one for Zest Brew and one for calmora

Detox - slim - cleanse

Also needs to says 14 Day Brewreset

Target Market(s)

Young people

Industry/Entity Type

It Company

Colors
000000

Requirements
Must have
• #joinvividleaf
Nice to have
• Herbal tea supplement 50gram
• Max label size 13.5cm x 16.5 cm
• Personally I like the paper brown bag as it looks like a higher quality and as the label is a sticker I think this would make the product look a lot better
Should not have
• Nothing

```html
<!DOCTYPE html>
<html lang="en">
<head>
<meta charset="utf-8">
<title>Join Vivid Leaf – Tea Labels</title>
<link href="https://fonts.googleapis.com/css2?family=Montserrat:wght@500;600;700&family=Arimo:wght@400;700&display=swap" rel="stylesheet">
<style>
  :root{
    --bg:#000000;
    --heading:#5a5a5a;
    --zest-orange:#f7941d;
    --zest-orange-deep:#ef8518;
    --zest-ink:#2a2116;
    --zest-tag:#f6e31c;
    --zest-ribbon:#8cc63f;
    --zest-leaf:#a6d84a;
    --seal-gold:#e9b21a;
    --calm-navy:#1b2d8f;
    --calm-navy-deep:#0a1142;
    --calm-ink:#ffffff;
    --calm-ribbon:#29b6ea;
    --calm-flower:#5063c9;
    --seal-grey:#8d9096;
  }
  *{margin:0;padding:0;box-sizing:border-box}
  html,body{width:1200px;height:968px;overflow:hidden;background:var(--bg)}
  .canvas{position:relative;width:1200px;height:968px;background:var(--bg)}

  .brand-heading{position:absolute;left:66px;top:34px;font-family:"Montserrat",sans-serif;font-weight:700;color:var(--heading);line-height:1}
  .brand-heading .kicker{display:block;font-size:34px;letter-spacing:-0.5px}
  .brand-heading .name{display:block;font-size:70px;letter-spacing:-2px;margin-top:2px}

  .label{position:absolute;top:340px;width:300px;height:420px;border-radius:8px;overflow:hidden}
  .label--zest{left:250px;background:linear-gradient(180deg,var(--zest-orange) 0%,var(--zest-orange-deep) 100%)}
  .label--calm{left:660px;background:radial-gradient(ellipse at 50% 30%,var(--calm-navy) 0%,var(--calm-navy-deep) 100%)}

  .seal{position:absolute;left:34px;top:64px;width:46px;height:46px;border-radius:50%}
  .label--zest .seal{background:var(--seal-gold);border:3px solid #fff3b0}
  .label--calm .seal{background:var(--seal-grey);border:3px solid #d7d9dd}

  .ribbon{position:absolute;right:0;top:60px;padding:4px 12px 4px 10px;font-family:"Arimo",sans-serif;color:#fff;line-height:1;text-align:center}
  .ribbon .days{display:block;font-size:20px}
  .ribbon .plan{display:block;font-size:10px;letter-spacing:0.5px;margin-top:2px}
  .label--zest .ribbon{background:var(--zest-ribbon);color:#fff8d0}
  .label--calm .ribbon{background:var(--calm-ribbon)}

  .title{position:absolute;left:0;right:0;top:122px;text-align:center;font-family:"Montserrat",sans-serif;font-weight:700;line-height:1}
  .title .kicker{display:block;font-size:20px;font-weight:600}
  .title .name{display:block;font-size:46px;letter-spacing:-1.5px;margin-top:6px}
  .label--zest .title{color:var(--zest-ink)}
  .label--calm .title{color:var(--calm-ink)}

  .variant{position:absolute;left:0;right:0;top:214px;text-align:center;font-family:"Arimo",sans-serif}
  .variant-tag{display:inline-block;background:var(--zest-tag);border:2px solid var(--zest-ink);padding:3px 12px;font-size:15px;font-weight:700;letter-spacing:1px;color:var(--zest-ink)}
  .variant-line{display:inline-flex;align-items:center;gap:8px;font-size:15px;letter-spacing:4px;color:var(--calm-ink)}

  .claims{position:absolute;left:0;right:0;top:262px;text-align:center;font-family:"Arimo",sans-serif;font-size:14px;letter-spacing:0.3px}
  .label--zest .claims{color:var(--zest-ink)}
  .label--calm .claims{color:var(--calm-ink);top:282px}

  .weight{position:absolute;left:0;right:0;bottom:30px;text-align:center;font-family:"Arimo",sans-serif;font-size:11px;z-index:2}
  .label--zest .weight{color:var(--zest-ink)}
  .label--calm .weight{color:var(--calm-ink);bottom:78px}

  .ornament{position:absolute;left:0;right:0;bottom:0;height:130px}
  .label--zest .ornament{background:linear-gradient(180deg,rgba(166,216,74,0) 0%,rgba(166,216,74,0.55) 100%)}
  .label--calm .ornament{height:150px;background:linear-gradient(180deg,rgba(80,99,201,0) 0%,rgba(80,99,201,0.6) 100%)}
</style>
</head>
<body>
<main class="canvas">
  <h1 class="brand-heading"><span class="kicker">Join</span><span class="name">Vivid Leaf</span></h1>

  <section class="label label--zest" aria-label="Zest Brew day label">
    <div class="seal" aria-hidden="true"></div>
    <div class="ribbon"><span class="days">14</span><span class="plan">DAY BREWRESET</span></div>
    <h2 class="title"><span class="kicker">Join</span><span class="name">Vivid Leaf</span></h2>
    <div class="variant"><span class="variant-tag">ZEST BREW</span></div>
    <p class="claims">DETOX - SLIM - CLEANSE</p>
    <div class="ornament" role="img" aria-label="Green leafy vine ornament along the bottom of the label"></div>
    <p class="weight">50gram</p>
  </section>

  <section class="label label--calm" aria-label="Calmora night label">
    <div class="seal" aria-hidden="true"></div>
    <div class="ribbon"><span class="days">14</span><span class="plan">DAY BREWRESET</span></div>
    <h2 class="title"><span class="kicker">Join</span><span class="name">Vivid Leaf</span></h2>
    <div class="variant">
      <span class="variant-line">CALMORA
        <svg width="18" height="18" viewBox="0 0 18 18" aria-hidden="true"><path d="M12 2a7 7 0 1 0 4 12.5A6 6 0 0 1 12 2z" fill="#ffffff"/></svg>
      </span>
    </div>
    <p class="claims">DETOX - SLIM - CLEANSE</p>
    <p class="weight">50gram</p>
    <div class="ornament" role="img" aria-label="Soft blue floral ornament along the bottom of the label"></div>
  </section>
</main>
</body>
</html>
```